Boutique Technology Consultancy specialising is Electronic and physical security

We need to redo our existing outdated website. For your reference the link www.bimo.com.au

```html
<!DOCTYPE html>
<html lang="en">
<head>
<meta charset="utf-8">
<title>BIMO Services – Technology Projects Made Easy</title>
<link href="https://fonts.googleapis.com/css2?family=Lexend:wght@400;500;600&family=Poppins:wght@400;500;600&display=swap" rel="stylesheet">
<style>
:root{
  --red:#c8201f;
  --dark:#0a0e18;
  --navy:#111726;
  --blue:#2f4a6b;
  --grey:#efefef;
  --white:#ffffff;
  --text:#222222;
  --muted:#555b66;
}
*{margin:0;padding:0;box-sizing:border-box}
html,body{width:1200px;height:4325px;overflow:hidden}
body{font-family:"Poppins",sans-serif;color:var(--text);background:var(--white);position:relative}
h1,h2,h3,h4,.brand{font-family:"Lexend",sans-serif}
section,header,footer{position:absolute;left:0;width:1200px}
.abs{position:absolute}
.red-rule{position:absolute;height:5px;background:var(--red)}
.btn{position:absolute;display:flex;align-items:center;justify-content:space-between;padding:0 6px 0 32px;border-radius:20px;background:var(--red);color:#fff;font:500 14px "Poppins",sans-serif}
.btn .arrow{width:26px;height:26px;border-radius:50%;background:#fff;display:flex;align-items:center;justify-content:center}
.btn-dark{background:linear-gradient(90deg,#3a0d0d,#7a1414 60%,var(--red))}

/* hero */
.hero{top:0;height:739px;background:radial-gradient(ellipse at 20% 40%,#2a0c10 0%,var(--dark) 55%);overflow:hidden}
.topbar{position:absolute;top:0;left:0;width:1200px;height:50px;border-bottom:1px solid #262b38;display:flex;align-items:center;font-size:12px;color:#dfe2e8}
.topbar span{position:absolute}
.social-dot{position:absolute;width:18px;height:18px;border-radius:50%;border:1.5px solid #cfd3da}
.nav{position:absolute;top:50px;left:0;width:1200px;height:60px}
.brand{font-weight:600;color:#fff;letter-spacing:1px}
.nav ul{position:absolute;left:385px;top:26px;display:flex;gap:34px;list-style:none;font-size:13px;color:#e6e8ec}
.nav li.active{font-weight:600;color:#fff}
.hero h1{position:absolute;left:125px;top:200px;font-size:62px;line-height:74px;font-weight:600;color:#fff}
.hero .bar{position:absolute;left:105px;top:218px;width:5px;height:200px;background:var(--red)}
.hero p{position:absolute;left:125px;top:430px;width:330px;font-size:14px;line-height:21px;color:#e2e4ea}
.hero-photo{position:absolute;left:792px;top:140px;width:480px;height:620px;border-radius:240px 0 0 60px;background:linear-gradient(160deg,#d9cbbb,#b07a45 55%,#e07a2c)}

/* about */
.about{top:739px;height:664px;background:#fff}
.dots{position:absolute;left:112px;top:160px;width:42px;height:370px;background-image:radial-gradient(var(--red) 2px,transparent 2.5px);background-size:10px 10px}
.about-photo{position:absolute;left:147px;top:131px;width:467px;height:425px;border-radius:16px;background:linear-gradient(135deg,#cfd4dc,#8c97a8 50%,#e9e3da)}
.about h2{position:absolute;left:717px;top:165px;font-size:44px;font-weight:600;color:var(--text)}
.about h4{position:absolute;left:717px;top:228px;width:340px;font-size:12px;line-height:18px;font-weight:600}
.about p{position:absolute;left:717px;top:280px;width:340px;font-size:12px;line-height:19px;color:var(--muted)}

/* services */
.services{top:1403px;height:464px;background:linear-gradient(135deg,#070a12,#141b2c 60%,#0b0f1a);color:#fff}
.services h2{position:absolute;left:125px;top:110px;font-size:44px;font-weight:600}
.service{position:absolute;top:235px;width:215px}
.service h3{font-size:18px;font-weight:500;margin-bottom:10px;font-family:"Poppins",sans-serif;white-space:nowrap}
.service p{font-size:12px;line-height:18px;color:#cdd1d9}
.service .more{display:inline-block;margin-top:18px;font-size:11px;font-weight:600;border-bottom:2px solid #fff;letter-spacing:.5px}
.service-icon{position:absolute;left:-72px;top:38px}

/* why */
.why{top:1867px;height:694px;background:#fff;text-align:center}
.why h2,.blog h2{position:absolute;left:0;width:1200px;text-align:center;font-size:42px;font-weight:600;color:var(--dark)}
.lead{position:absolute;left:300px;width:600px;font-size:12px;line-height:18px;color:var(--muted);text-align:center}
.card{position:absolute;top:316px;border-radius:12px;background:var(--grey);padding:90px 30px 0;text-align:center}
.card.featured{background:#fff;box-shadow:0 10px 32px rgba(0,0,0,.18)}
.card h3{font-family:"Poppins",sans-serif;font-size:18px;font-weight:500;line-height:22px;margin-bottom:12px}
.card p{font-size:11px;line-height:19px;color:var(--muted)}
.card .read{margin-top:18px;font-size:11px;font-weight:600;color:var(--red);display:inline-flex;align-items:center;gap:12px}
.card .read i{width:20px;height:20px;border-radius:50%;background:var(--red);display:inline-block}
.badge{position:absolute;left:50%;transform:translateX(-50%);top:-6px;width:80px;height:80px;border-radius:50%;background:#fff;display:flex;align-items:center;justify-content:center}
.featured .badge{top:-30px;width:100px;height:100px;border:4px solid var(--dark)}

/* team */
.team{top:2561px;height:648px;background:linear-gradient(135deg,#0a0e18,#131a2b 55%,#090c14);color:#fff}
.team h2{position:absolute;left:119px;top:114px;font-size:44px;font-weight:600}
.team .intro{position:absolute;left:119px;top:180px;width:440px;font-size:12px;line-height:19px;color:#dfe2e8}
.slide{position:absolute;top:281px;height:264px}
.member{padding:34px 22px}
.member h3{font-family:"Poppins",sans-serif;font-size:17px;font-weight:500;margin-bottom:22px}
.member p{font-size:11px;line-height:18px;color:#eef0f3}
.pager{position:absolute;left:22px;bottom:22px;width:42px;height:42px;border-radius:50%;background:rgba(255,255,255,.55);display:flex;align-items:center;justify-content:center}
.portrait{background:linear-gradient(160deg,#e9e6e2,#9a9fa8 55%,#2b2f38)}

/* blog */
.blog{top:3209px;height:686px;background:#fff}
.post{position:absolute;top:258px;width:306px}
.post-photo{height:270px;background:linear-gradient(150deg,#b7a48c,#4c5260 60%,#26324a)}
.post-box{position:absolute;left:16px;top:232px;width:290px;background:var(--dark);color:#fff;padding:14px 16px 16px;border-left:4px solid var(--red)}
.meta{display:flex;gap:34px;font-size:10px;color:#d3d6dc;margin-bottom:10px}
.post h3{font-family:"Poppins",sans-serif;font-size:16px;line-height:20px;font-weight:600}
.post .read{margin-top:14px;font-size:11px;font-weight:600;color:var(--red);display:flex;align-items:center;gap:12px}
.post .read i{width:18px;height:18px;border-radius:50%;background:var(--red)}

/* footer */
.footer{top:3895px;height:369px;background:linear-gradient(135deg,#1a0609,#0a0c12 45%,#14060a);color:#fff}
.footer .brand{position:absolute;left:125px;top:70px;font-size:56px}
.footer .brand small{display:block;font-size:16px;letter-spacing:10px;font-weight:600;margin-top:-4px}
.f-social{position:absolute;top:200px;width:40px;height:40px;border-radius:50%;border:2px solid #fff}
.footer h4{position:absolute;top:60px;font-size:22px;font-weight:400}
.quick{position:absolute;left:564px;top:118px;list-style:none;font-size:13px;line-height:40px}
.contact{position:absolute;left:870px;display:flex;align-items:center;gap:24px;font-size:12px;line-height:19px}
.contact .ic{width:44px;height:44px;border-radius:50%;background:#fff;display:flex;align-items:center;justify-content:center;flex:none}
.copyright{position:absolute;left:0;top:4264px;width:1200px;height:61px;background:#111317;color:#fff;font-size:13px;display:flex;align-items:center;justify-content:center}
</style>
</head>
<body>

<header class="hero">
  <div class="topbar">
    <svg class="abs" style="left:138px;top:18px" width="16" height="12" viewBox="0 0 16 12"><rect x="0.5" y="0.5" width="15" height="11" fill="none" stroke="#fff"/><path d="M1 1 L8 7 L15 1" fill="none" stroke="#fff"/></svg>
    <span style="left:164px">hello@bimo.com.au</span>
    <span style="left:342px">(+) 1300 555 010</span>
    <span style="left:497px">Melbourne Vic 3000</span>
    <i class="social-dot" style="left:896px;top:16px"></i>
    <i class="social-dot" style="left:934px;top:16px"></i>
    <i class="social-dot" style="left:972px;top:16px"></i>
    <i class="social-dot" style="left:1010px;top:16px"></i>
    <i class="social-dot" style="left:1048px;top:16px"></i>
  </div>
  <nav class="nav">
    <div class="brand abs" style="left:125px;top:14px;font-size:30px;display:flex;align-items:center;gap:8px"><i style="width:14px;height:14px;background:var(--red);display:inline-block"></i>BIMO</div>
    <ul>
      <li class="active">Home</li><li>Experience</li><li>Our Services</li><li>Our Team</li><li>About</li><li>Contact Us</li>
    </ul>
    <svg class="abs" style="left:990px;top:24px" width="18" height="18" viewBox="0 0 18 18"><circle cx="7.5" cy="7.5" r="6" fill="none" stroke="#fff" stroke-width="1.6"/><path d="M12 12 L17 17" stroke="#fff" stroke-width="1.6"/></svg>
    <svg class="abs" style="left:1034px;top:24px" width="44" height="18" viewBox="0 0 44 18"><path d="M0 3 H44 M12 15 H44" stroke="#fff" stroke-width="2"/></svg>
  </nav>
  <div class="bar"></div>
  <h1>Your Technology<br>Projects Made<br>Easy</h1>
  <p>Lorem Ipsum is simply dummy text of the printing and typesetting industry. Lorem Ipsum has been the</p>
  <div class="btn btn-dark" style="left:125px;top:530px;width:156px;height:37px">Learn More <span class="arrow"><svg width="12" height="10" viewBox="0 0 12 10"><path d="M0 5 H10 M6 1 L10 5 L6 9" fill="none" stroke="#111" stroke-width="1.6"/></svg></span></div>
  <div class="hero-photo" role="img" aria-label="Smiling consultant in an orange sweater holding a tablet"></div>
</header>
<svg class="abs" style="left:1110px;top:739px;z-index:2" width="90" height="82" viewBox="0 0 90 82"><path d="M0 0 H90 V82 Z" fill="#0a0e18"/></svg>

<section class="about">
  <div class="dots"></div>
  <div class="about-photo" role="img" aria-label="Team of three colleagues reviewing documents at a desk"></div>
  <div class="red-rule" style="left:720px;top:156px;width:130px"></div>
  <h2>About Us</h2>
  <h4>Lorem Ipsum Is Simply Dummy Text Of The Printing And Typesetting Industry. Lorem Ip</h4>
  <p>Lorem Ipsum is simply dummy text of the printing and typesetting industry. Lorem Ipsum has been the industry's standard dummy text ever since the 1500s, when an unknown printer took a galley of type Lorem Ipsum is simply dummy text of the printing and typesetting industry. Lorem Ipsum has been the industry's sta</p>
  <div class="btn btn-dark" style="left:717px;top:461px;width:156px;height:37px">Read More <span class="arrow"><svg width="12" height="10" viewBox="0 0 12 10"><path d="M0 5 H10 M6 1 L10 5 L6 9" fill="none" stroke="#111" stroke-width="1.6"/></svg></span></div>
</section>

<section class="services">
  <div class="red-rule" style="left:125px;top:97px;width:125px"></div>
  <h2>Our Services</h2>
  <div class="btn" style="left:917px;top:142px;width:153px;height:34px;padding-left:36px">See All <span class="arrow" style="width:24px;height:24px"><svg width="12" height="10" viewBox="0 0 12 10"><path d="M0 5 H10 M6 1 L10 5 L6 9" fill="none" stroke="#111" stroke-width="1.6"/></svg></span></div>

  <div class="service" style="left:195px">
    <svg class="service-icon" width="52" height="46" viewBox="0 0 52 46"><rect x="2" y="6" width="48" height="36" rx="4" fill="#fff"/><path d="M10 16 H42 M10 24 H42 M10 32 H30" stroke="#141b2c" stroke-width="3"/></svg>
    <h3>Project</h3>
    <p>Lorem Ipsum is simply dummy text of the printing and typesetting in and typesetting in</p>
    <span class="more">MORE</span>
  </div>
  <div class="service" style="left:511px">
    <svg class="service-icon" width="52" height="50" viewBox="0 0 52 50"><path d="M4 44 V30 M14 44 V22 M24 44 V14 M34 44 V24" stroke="#fff" stroke-width="6"/><circle cx="40" cy="36" r="7" fill="none" stroke="#fff" stroke-width="3"/><path d="M45 41 L51 48" stroke="#fff" stroke-width="3"/></svg>
    <h3>Strategy</h3>
    <p>Lorem Ipsum is simply dummy text of the printing and typesetting in and typesetting in</p>
    <span class="more">MORE</span>
  </div>
  <div class="service" style="left:825px">
    <svg class="service-icon" width="52" height="50" viewBox="0 0 52 50"><circle cx="20" cy="28" r="13" fill="none" stroke="#fff" stroke-width="7" stroke-dasharray="6 4"/><circle cx="20" cy="28" r="5" fill="#fff"/><circle cx="40" cy="12" r="8" fill="none" stroke="#fff" stroke-width="5" stroke-dasharray="4 3"/></svg>
    <h3>Operations And Maintenance</h3>
    <p>Lorem Ipsum is simply dummy text of the printing and typesetting in and typesetting in</p>
    <span class="more">MORE</span>
  </div>
</section>

<section class="why">
  <div class="red-rule" style="left:555px;top:102px;width:90px"></div>
  <h2 style="top:110px">Why Choose Us</h2>
  <p class="lead" style="top:181px">Lorem Ipsum is simply dummy text of the printing and typesetting industry. Lorem Ipsum has been the industry's standard dummy t</p>

  <div class="card featured" style="left:111px;width:314px;height:276px">
    <div class="badge"><svg width="56" height="56" viewBox="0 0 56 56"><circle cx="28" cy="28" r="27" fill="var(--red)"/><rect x="16" y="14" width="18" height="26" fill="#fff"/><path d="M20 20 H30 M20 26 H30 M20 32 H30" stroke="var(--red)" stroke-width="2"/><circle cx="37" cy="36" r="7" fill="#fff"/></svg></div>
    <h3>Property/Facilities<br>Management</h3>
    <p>Lorem Ipsum is simply dummy text of the printing and typesetting industry. Lorem Ipsum has been the industry's standard dummy text ever since the 1500s,</p>
    <span class="read">READ MORE <i></i></span>
  </div>
  <div class="card" style="left:444px;width:312px;height:260px">
    <div class="badge"><svg width="52" height="52" viewBox="0 0 52 52"><circle cx="26" cy="26" r="25" fill="var(--red)"/><rect x="16" y="22" width="20" height="16" rx="2" fill="#fff"/><path d="M20 22 V17 a6 6 0 0 1 12 0 V22" fill="none" stroke="#fff" stroke-width="3"/></svg></div>
    <h3>Asset Management</h3>
    <p>Lorem Ipsum is simply dummy text of the printing and typesetting industry. Lorem Ipsum has been the industry's standard dummy text ever since the 1500s,</p>
    <span class="read">READ MORE <i></i></span>
  </div>
  <div class="card" style="left:772px;width:303px;height:280px">
    <div class="badge"><svg width="52" height="52" viewBox="0 0 52 52"><circle cx="26" cy="26" r="25" fill="var(--red)"/><path d="M14 30 a12 12 0 0 1 24 0 Z" fill="#fff"/><rect x="12" y="30" width="28" height="4" fill="#fff"/><rect x="18" y="36" width="16" height="6" fill="#fff"/></svg></div>
    <h3>Development And<br>Construction</h3>
    <p>Lorem Ipsum is simply dummy text of the printing and typesetting industry. Lorem Ipsum has been the industry's standard dummy text ever since the 1500s,</p>
    <span class="read">READ MORE <i></i></span>
  </div>
</section>

<section class="team">
  <div class="red-rule" style="left:119px;top:102px;width:95px"></div>
  <h2>Our Team</h2>
  <p class="intro">Lorem Ipsum is simply dummy text of the printing and typesetting industry. Lorem Ipsum has been the industry's standard dummy t ondard dummy t</p>

  <div class="slide member" style="left:119px;width:233px;background:var(--blue)">
    <h3>Nora Quinn</h3>
    <p>Lorem Ipsum is simply dummy text of the printing and typesetting industry. Lorem Ipsum has been the industry's standard dum</p>
    <span class="pager"><svg width="16" height="12" viewBox="0 0 16 12"><path d="M16 6 H2 M6 1 L1 6 L6 11" fill="none" stroke="#fff" stroke-width="1.8"/></svg></span>
  </div>
  <div class="slide portrait" style="left:352px;width:245px" role="img" aria-label="Portrait of team member in a dark suit"></div>
  <div class="slide member" style="left:597px;width:242px;background:var(--red)">
    <h3>Owen Hale</h3>
    <p>Lorem Ipsum is simply dummy text of the printing and typesetting industry. Lorem Ipsum has been the industry's standard dum</p>
    <span class="pager"><svg width="16" height="12" viewBox="0 0 16 12"><path d="M0 6 H14 M10 1 L15 6 L10 11" fill="none" stroke="#fff" stroke-width="1.8"/></svg></span>
  </div>
  <div class="slide portrait" style="left:839px;width:242px" role="img" aria-label="Portrait of team member in a grey suit"></div>
</section>

<section class="blog">
  <div class="red-rule" style="left:555px;top:102px;width:90px"></div>
  <h2 style="top:108px">Latest News &amp; Blog</h2>
  <p class="lead" style="top:174px">Lorem Ipsum is simply dummy text of the printing and typesetting industry. Lorem Ipsum has been the industry's standard dummy t ondard dummy t</p>

  <article class="post" style="left:125px">
    <div class="post-photo" role="img" aria-label="Two businessmen talking in an office"></div>
    <div class="post-box"><div class="meta"><span>By Admin</span><span>Comments (3)</span></div><h3>Lorem Ipsum Is Simply Dummy Text Of The</h3></div>
  </article>
  <article class="post" style="left:450px">
    <div class="post-photo" role="img" aria-label="Colleagues reviewing a tablet together"></div>
    <div class="post-box"><div class="meta"><span>By Admin</span><span>Comments (3)</span></div><h3>Lorem Ipsum Is Simply Dummy Text Of The</h3><span class="read">READ MORE <i></i></span></div>
  </article>
  <article class="post" style="left:775px;width:300px">
    <div class="post-photo" style="background:linear-gradient(150deg,#f2f0ec,#c9c4bc 50%,#3b4354)" role="img" aria-label="Business partners working at a laptop"></div>
    <div class="post-box" style="width:284px"><div class="meta"><span>By Admin</span><span>Comments (3)</span></div><h3>Lorem Ipsum Is Simply Dummy Text Of The</h3></div>
  </article>
</section>

<footer class="footer">
  <div class="brand">BIMO<small>SERVICES</small></div>
  <i class="f-social" style="left:125px"></i>
  <i class="f-social" style="left:180px"></i>
  <i class="f-social" style="left:235px"></i>
  <i class="f-social" style="left:290px"></i>
  <h4 style="left:564px">Quick Links</h4>
  <ul class="quick"><li>Home</li><li>About Us</li><li>Our Services</li><li>Experience</li><li>Our Team</li><li>Contact Us</li></ul>
  <h4 style="left:870px">Contact Us</h4>
  <div class="contact" style="top:120px"><span class="ic"><svg width="14" height="18" viewBox="0 0 14 18"><path d="M7 17 C7 17 1 10 1 6.5 a6 6 0 0 1 12 0 C13 10 7 17 7 17Z" fill="var(--red)"/><circle cx="7" cy="6.5" r="2.2" fill="#fff"/></svg></span><span>Level 2, 88 Harbour<br>St Melbourne VIC 3000</span></div>
  <div class="contact" style="top:197px"><span class="ic"><svg width="16" height="16" viewBox="0 0 16 16"><path d="M1 8 L15 1 L10 15 L8 9 Z" fill="var(--red)"/></svg></span><span>hello@bimo.com.au</span></div>
  <div class="contact" style="top:285px"><span class="ic"><svg width="16" height="16" viewBox="0 0 16 16"><path d="M3 1 L6 1 L7 5 L5 6.5 C6 9 7 10 9.5 11 L11 9 L15 10 L15 13 C15 14 14 15 13 15 C6 15 1 10 1 3 C1 2 2 1 3 1Z" fill="var(--red)"/></svg></span><span>1300 555 010</span></div>
</footer>
<div class="copyright">© Copyright 2023&nbsp;<strong>BIMO Services</strong>&nbsp;. All Rights Reserved</div>

</body>
</html>
```